Start up business website

IT Support provider that caters towards law enforcement / police departments. We'll offer remote IT support, backup / recovery services and cyber security. Will add updates soon.

Target Market(s)

Police departments / Law Enforcement

Coding

Coded - Design and coding required

Number of Pages Required

5+ page

Other font styles liked:
• Use font style in uploaded logo

Colors
0054AA
0677BA
7BADD7
CADEEF
E8F1F8

```html
<!DOCTYPE html>
<html lang="en">
<head>
<meta charset="utf-8">
<title>Ironward Support Services</title>
<link rel="stylesheet" href="https://fonts.googleapis.com/css2?family=Krona+One&family=Roboto:wght@400;500;700&display=swap">
<style>
:root{
  --blue:#0054AA;
  --blue-mid:#0677BA;
  --blue-soft:#7BADD7;
  --blue-pale:#CADEEF;
  --blue-mist:#E8F1F8;
  --navy:#020a1c;
  --navy-2:#06183a;
  --ink:#111;
  --grey-text:#555;
  --light:#f2f3f5;
  --white:#fff;
}
*{box-sizing:border-box;margin:0;padding:0}
html,body{width:1200px;height:4360px;overflow:hidden}
body{font-family:'Roboto',sans-serif;color:var(--ink);background:var(--white);position:relative}
section,header,footer{position:absolute;left:0;width:1200px;overflow:hidden}
.abs{position:absolute}
.display{font-family:'Krona One',sans-serif;text-transform:uppercase;letter-spacing:1px;white-space:nowrap}
.btn{display:inline-block;font-family:'Roboto',sans-serif;font-size:15px;font-weight:500;text-transform:uppercase;border-radius:24px;padding:14px 34px;letter-spacing:.5px}
.btn-solid{background:var(--blue);color:var(--white)}
.btn-outline{border:1.5px solid var(--blue);color:var(--blue);background:var(--white)}
.body-copy{font-size:15px;line-height:26px;color:var(--grey-text)}
.ph{position:absolute}

/* hero */
.hero{top:0;height:680px;background:radial-gradient(circle at 75% 45%,#0b3d8c 0%,#05205a 30%,var(--navy) 70%)}
.hero-visual{left:560px;top:60px;width:600px;height:580px;border-radius:50%;background:radial-gradient(circle,#2a8ef0 0%,#0c4fb0 35%,rgba(4,24,70,0) 70%);opacity:.85}
.nav{left:0;top:0;width:1200px;height:80px;display:flex;align-items:center;padding:0 96px 0 110px;justify-content:space-between}
.brand{display:flex;align-items:center;gap:12px;color:var(--white);font-family:'Krona One',sans-serif;font-size:19px;text-transform:uppercase}
.brand-mark{width:26px;height:26px;border-radius:50%;background:var(--blue-mid)}
.nav-links{display:flex;gap:40px;list-style:none}
.nav-links li{color:var(--white);font-size:16px}
.hero-title{left:120px;top:205px;color:var(--white);font-size:74px;line-height:84px}
.hero-sub{left:120px;top:290px;color:var(--white);font-size:29px;line-height:36px}
.hero-text{left:120px;top:340px;width:420px;color:var(--white);font-size:16px;line-height:24px}
.hero .btn{position:absolute;left:120px;top:410px}
.arrow{top:320px;width:24px;height:40px}
.dots{left:550px;top:620px;display:flex;gap:10px}
.dots span{width:10px;height:10px;border-radius:50%;border:1.5px solid var(--white)}
.dots span.on{background:var(--white)}

/* about */
.about{top:680px;height:610px;background:linear-gradient(180deg,#eceef1,#f7f8fa)}
.about-visual{left:120px;top:70px;width:310px;height:430px;border-radius:40px 40px 155px 155px;background:linear-gradient(160deg,#1d2a45,#0f4f9c 60%,#c9d3df)}
.eyebrow{font-size:15px;color:var(--blue);letter-spacing:1px;text-transform:uppercase}
.about-copy{left:620px;top:95px;width:480px}
.about-copy h2{font-size:34px;line-height:44px;color:var(--blue);margin-top:8px}
.about-copy h3{font-size:22px;line-height:30px;color:var(--ink);margin-bottom:16px}
.about-copy .btn{margin-top:28px}

/* services */
.services{top:1290px;height:790px;background:radial-gradient(ellipse at 50% 80%,#0a2e6b 0%,var(--navy-2) 40%,var(--navy) 80%)}
.services h2{top:95px;width:1200px;text-align:center;font-size:42px;line-height:52px}
.services h2 .accent{color:var(--blue-mid)}
.services h2 .plain{color:var(--white)}
.services-visual{left:180px;top:280px;width:300px;height:300px;border-radius:50%;background:radial-gradient(circle,#2b5d9c,#0e2550 70%);border:4px solid #c7ccd4}
.service-list{left:600px;top:0;width:500px;height:790px;list-style:none}
.service-list li{position:absolute;display:flex;align-items:center;gap:20px;color:var(--white);font-size:24px;font-weight:500;text-transform:uppercase}
.svc-icon{width:46px;height:46px;border-radius:50%;background:var(--white);display:flex;align-items:center;justify-content:center}

/* experts */
.experts{top:2080px;height:540px;background:var(--white)}
.experts-visual{left:560px;top:0;width:640px;height:540px;border-radius:270px 0 0 270px;background:linear-gradient(120deg,#10213f,#2a5488 45%,#d6dbe2)}
.experts-copy{left:100px;top:115px;width:430px}
.experts-copy h2{font-size:40px;line-height:50px;margin-bottom:22px}
.experts-copy h2 .accent{color:var(--blue)}
.experts-copy .btn{margin-top:26px}
.title-rule{left:0;top:140px;width:80px;height:3px;background:var(--blue)}

/* news */
.news{top:2620px;height:760px;background:var(--white)}
.news h2{top:105px;width:1200px;text-align:center;font-size:40px;line-height:50px}
.news h2 .accent{color:var(--blue)}
.news-feature{left:100px;top:180px;width:480px;height:440px;background:linear-gradient(180deg,#3b4e6a,#1a2233)}
.news-feature .meta{position:absolute;left:30px;bottom:30px;width:420px;color:var(--white)}
.date-tag{display:inline-block;background:var(--blue);color:var(--white);font-size:13px;padding:7px 14px;margin-bottom:12px}
.news-feature h3{font-size:19px;line-height:25px;font-weight:700}
.news-feature p{font-size:14px;line-height:20px;margin-top:6px}
.news-card{left:600px;width:505px;height:205px;border:1px solid var(--blue-pale);background:var(--white)}
.news-card .thumb{position:absolute;left:0;top:0;width:205px;height:203px;background:linear-gradient(150deg,#3a5b86,#182640)}
.news-card .meta{position:absolute;left:225px;top:22px;width:260px}
.news-card h3{font-size:16px;line-height:21px;font-weight:700}
.news-card p{font-size:13px;line-height:19px;color:var(--grey-text);margin-top:4px}

/* contact */
.contact{top:3380px;height:580px;background:linear-gradient(180deg,#e3e4e6,#f0f1f3)}
.contact h2{left:100px;top:112px;font-size:40px;line-height:50px}
.contact h2 .accent{color:var(--blue)}
.field{position:absolute;background:var(--white);font-size:13px;color:#666;padding:14px 16px;height:46px}
.contact .btn{position:absolute;left:100px;top:450px;border-radius:4px;padding:12px 26px;font-size:14px}
.contact-visual{left:720px;top:55px;width:350px;height:480px;border-radius:40px 40px 175px 175px;background:linear-gradient(160deg,#1c2a44,#1c5aa4 55%,#d0d6de)}

/* footer */
.footer{top:3960px;height:400px;background:#000;color:var(--white)}
.badge{left:100px;top:75px;width:290px;height:140px;background:linear-gradient(180deg,#6a6a6a,#3a3a3a);border:2px solid #888}
.foot-col{top:90px}
.foot-col h4{font-size:15px;font-weight:700;text-transform:uppercase;margin-bottom:14px}
.foot-col ul{list-style:none}
.foot-col li{font-size:12.5px;line-height:24px;color:#ddd}
.contact-line{display:flex;align-items:center;gap:10px;font-size:12.5px;line-height:18px;color:#ddd;margin-bottom:16px}
.copyright{left:0;top:345px;width:1200px;text-align:center;font-size:13px;color:#ccc}
.foot-rule{left:0;top:320px;width:1200px;height:1px;background:#222}
</style>
</head>
<body>

<header class="hero">
  <div class="ph hero-visual" role="img" aria-label="Glowing digital security interface with padlock and shield graphics"></div>
  <nav class="abs nav">
    <div class="brand"><span class="brand-mark"></span>Ironward</div>
    <ul class="nav-links">
      <li>Home</li><li>Services</li><li>About us</li><li>Follow up</li><li>CJIS Compliance</li><li>Contact us</li>
    </ul>
  </nav>
  <h1 class="abs display hero-title">Ironward</h1>
  <p class="abs display hero-sub">Support Services</p>
  <p class="abs hero-text">Lorem ipsum dolor sit amet, consectetur adipiscing elit, sed do eiusmod tempor incididunt</p>
  <a class="btn btn-solid">Get Started</a>
  <svg class="abs arrow" style="left:45px" viewBox="0 0 24 40"><polyline points="20,2 4,20 20,38" fill="none" stroke="#fff" stroke-width="2"/></svg>
  <svg class="abs arrow" style="left:1131px" viewBox="0 0 24 40"><polyline points="4,2 20,20 4,38" fill="none" stroke="#fff" stroke-width="2"/></svg>
  <div class="abs dots"><span></span><span class="on"></span><span></span><span></span></div>
</header>

<section class="about">
  <div class="ph about-visual" role="img" aria-label="Shield-shaped photo of an officer working at a computer, framed with flag stripes"></div>
  <div class="abs about-copy">
    <p class="eyebrow">Who we are</p>
    <h2 class="display">About Ironward</h2>
    <h3 class="display">Support Services</h3>
    <p class="body-copy">Lorem ipsum dolor sit amet, consectetur adipiscing elit, sed do eiusmod tempor incididunt ut labore et dolore magna aliqua. Quis ipsum suspendisse ultrices gravida. Risus commodo viverra maecenas accumsan lacus vel facilisis. Lorem ipsum dolor sit amet, consectetur adipiscing elit, sed do eiusmod tempor incididunt ut labore et dolore magna aliqua. Quis ipsum suspendisse ultrices gravida. Risus commodo viverra maecenas accumsan lacus vel facilisis.</p>
    <a class="btn btn-outline">Learn More</a>
  </div>
</section>

<section class="services">
  <h2 class="abs display"><span class="accent">What</span> <span class="plain">We Offer</span></h2>
  <div class="ph services-visual" role="img" aria-label="Circular shield emblem photo of an officer at a computer"></div>
  <svg class="abs" style="left:0;top:0" width="1200" height="790" viewBox="0 0 1200 790">
    <g fill="none" stroke="#7BADD7" stroke-width="1.5" opacity=".8">
      <path d="M470 330 C520 270 540 260 600 255"/>
      <path d="M490 380 C540 345 560 335 620 335"/>
      <path d="M500 430 L 640 445"/>
      <path d="M490 480 C540 530 560 565 620 565"/>
      <path d="M470 530 C520 600 540 650 600 650"/>
      <path d="M430 250 C500 240 560 300 580 430 C560 560 500 620 430 610" stroke-dasharray="3 5"/>
    </g>
  </svg>
  <ul class="abs service-list">
    <li style="top:230px"><span class="svc-icon"><svg width="24" height="24" viewBox="0 0 24 24"><rect x="3" y="4" width="18" height="12" rx="1.5" fill="none" stroke="#0054AA" stroke-width="2"/><line x1="8" y1="20" x2="16" y2="20" stroke="#0054AA" stroke-width="2"/></svg></span>Remote IT Support</li>
    <li style="top:310px;left:20px"><span class="svc-icon"><svg width="24" height="24" viewBox="0 0 24 24"><path d="M19 12a7 7 0 1 1-2-5" fill="none" stroke="#0054AA" stroke-width="2"/><polyline points="18,3 18,8 13,8" fill="none" stroke="#0054AA" stroke-width="2"/></svg></span>Recovery Services</li>
    <li style="top:420px;left:40px"><span class="svc-icon"><svg width="24" height="24" viewBox="0 0 24 24"><rect x="5" y="11" width="14" height="10" rx="1.5" fill="#0054AA"/><path d="M8 11V8a4 4 0 0 1 8 0v3" fill="none" stroke="#0054AA" stroke-width="2"/></svg></span>Cyber Security</li>
    <li style="top:540px;left:20px"><span class="svc-icon"><svg width="24" height="24" viewBox="0 0 24 24"><ellipse cx="12" cy="6" rx="7" ry="3" fill="none" stroke="#0054AA" stroke-width="2"/><path d="M5 6v12c0 1.7 3 3 7 3s7-1.3 7-3V6" fill="none" stroke="#0054AA" stroke-width="2"/></svg></span>Data Protection</li>
    <li style="top:625px"><span class="svc-icon"><svg width="24" height="24" viewBox="0 0 24 24"><path d="M12 3 21 20H3Z" fill="none" stroke="#0054AA" stroke-width="2"/><line x1="12" y1="9" x2="12" y2="14" stroke="#0054AA" stroke-width="2"/><circle cx="12" cy="17" r="1.2" fill="#0054AA"/></svg></span>Risk Assessment</li>
  </ul>
</section>

<section class="experts">
  <div class="ph experts-visual" role="img" aria-label="Photo of IT specialists working at computer screens in an office"></div>
  <div class="abs title-rule"></div>
  <div class="abs experts-copy">
    <h2 class="display"><span class="accent">Our</span> Experts</h2>
    <p class="body-copy">Lorem ipsum dolor sit amet, consectetur adipiscing elit, sed do eiusmod tempor incididunt ut labore et dolore magna aliqua. Quis ipsum suspendisse ultrices gravida. Risus commodo viverra maecenas accumsan lacus vel facilisis. Lorem ipsum dolor sit amet, consectetur adipiscing elit, sed do eiusmod tempor incididunt ut labore.</p>
    <a class="btn btn-outline">Meet Our Expert</a>
  </div>
</section>

<section class="news">
  <h2 class="abs display"><span class="accent">News</span> &amp; Events</h2>
  <article class="abs news-feature" role="img" aria-label="Photo of a woman working on a laptop">
    <div class="meta">
      <span class="date-tag">13 Nov 2021</span>
      <h3>Lorem ipsum dolor sit amet, consectetur adipiscing elit, sed do eiusmod tempor incididunt</h3>
      <p>Lorem ipsum dolor sit amet, consectetur adipiscing elit, sed do eiusmod tempor</p>
    </div>
  </article>
  <article class="abs news-card" style="top:180px">
    <div class="thumb" role="img" aria-label="Photo of an IT technician at a monitor"></div>
    <div class="meta"><span class="date-tag">13 Nov 2021</span><h3>Lorem ipsum dolor sit amet, consectetur adipiscing elit, sed do</h3><p>Lorem ipsum dolor sit amet, consectetur adipiscing elit, sed do eiusmod tempor</p></div>
  </article>
  <article class="abs news-card" style="top:400px">
    <div class="thumb" role="img" aria-label="Photo of a team working at desks with computers"></div>
    <div class="meta"><span class="date-tag">13 Nov 2021</span><h3>Lorem ipsum dolor sit amet, consectetur adipiscing elit, sed do</h3><p>Lorem ipsum dolor sit amet, consectetur adipiscing elit, sed do eiusmod tempor</p></div>
  </article>
</section>

<section class="contact">
  <h2 class="abs display"><span class="accent">Contact</span> Form</h2>
  <div class="field" style="left:100px;top:195px;width:280px">First Name*</div>
  <div class="field" style="left:390px;top:195px;width:280px">Last Name*</div>
  <div class="field" style="left:100px;top:255px;width:280px">Contact Number*</div>
  <div class="field" style="left:390px;top:255px;width:280px">Email*</div>
  <div class="field" style="left:100px;top:315px;width:570px;height:110px">Leave a Message</div>
  <a class="btn btn-solid">Send Message</a>
  <div class="ph contact-visual" role="img" aria-label="Shield-shaped photo of an officer using a computer, framed with flag stripes"></div>
</section>

<footer class="footer">
  <div class="ph badge" role="img" aria-label="Veteran owned business badge"></div>
  <div class="abs foot-col" style="left:475px">
    <h4>Company</h4>
    <ul><li>Home</li><li>Services</li><li>About us</li><li>Follow up</li><li>CJIS Compliance</li><li>Contact us</li></ul>
  </div>
  <div class="abs foot-col" style="left:665px">
    <h4>Support</h4>
    <ul><li>Careers</li><li>Support</li><li>Sitemap</li><li>Privacy Policy</li><li>Contact Us</li></ul>
  </div>
  <div class="abs foot-col" style="left:875px;width:240px">
    <h4>Contact Us</h4>
    <p class="contact-line"><svg width="14" height="18" viewBox="0 0 14 18"><path d="M7 0a7 7 0 0 0-7 7c0 5 7 11 7 11s7-6 7-11a7 7 0 0 0-7-7Z" fill="#fff"/><circle cx="7" cy="7" r="2.5" fill="#000"/></svg>123 Your Address Goes Here,<br>CA 123456</p>
    <p class="contact-line"><svg width="16" height="16" viewBox="0 0 24 24"><path d="M6 2h4l2 5-3 2a11 11 0 0 0 6 6l2-3 5 2v4a2 2 0 0 1-2 2A18 18 0 0 1 4 4a2 2 0 0 1 2-2Z" fill="#fff"/></svg>000-000-0000</p>
    <p class="contact-line"><svg width="16" height="12" viewBox="0 0 16 12"><rect width="16" height="12" rx="1" fill="#fff"/><polyline points="1,1 8,7 15,1" fill="none" stroke="#000" stroke-width="1.5"/></svg>info@ironward-support.com</p>
  </div>
  <div class="abs foot-rule"></div>
  <p class="abs copyright">Copyright ©2021 Ironward Support Services. All rights reserved.</p>
</footer>

</body>
</html>
```